Revolutionary Video Platform (uncoded) - updated 05.11.

We want you to design the frontpage (uncoded) of FLIRTNOVA.net (we ev. hire the winner to create the subpages).

The concept of FLIRTNOVA.net is to show (ONLY!) infield videos of dating coaches (when they get in contact with women on the street) so that the users will have a solid base for deciding which coach they want to contact. I highlight that because some designs contained other ideas like "dating tips". No, we are specialized on infield videos. People should see if these coaches are really worth their money.

Therefore, the frontpage must include the following:

Header: Logo (attached), writing "FLIRTNOVA" or "FLIRT NOVA", links "Contact", "About", "Sign In", "Sign Up"

No design yet tried to change the logo in its size. You're welcome to do creative stuff.

What else is necessary on the front page:

1. 2 statements:

"Because 34 videos prove how to get every woman you want."
"Connect directly with 26 dating-coaches from these videos!"

The numbers should be showed in a way that the users know that they count up automatically; important: use the style zemlo has on it's front page by showing their amount of users.

2. Top rated Dating Coaches:

As the videos on the site can be rated, we want the coaches with the best rated videos on the front page with their faces (people can jump from there directly to their profiles).

To the pictures of the coaches you should also add the country flag and the city (where they come from). Plus, users should see who's on the first place, who's on the second place.. max. 10 coaches on the front page..

Set the title "TOP 10 DATING COACHES listed by best rated videos"

3. Search System

In order to find the videos the user is searching for, it needs a simple search form, where they can search after:

- Language
- Country
- City
- Rating
- Level of Difficulty
- Set-Size
- Conversation Starter

You can use simple white bars with a drop-down button.

4. Tags

Implement tags like "bitch shield, blow out opener, bounce, calibration, canned routine, challenge point, cockblock, cold approach, cold reading, compliment opener" etc.

Alphabetically listed..

5. Create previews of the (searched) videos which contains:

- Thumbnail of the video (only thumbnails on front page, no bigger video playback window, pls use pictures in order to make the site look more real)

- Some infos about the video (name of the coach with user-picture, duration, language, country (name and flag), city, audio comment (yes/no), difficulty level (super easy-expert), views, points needed to view (1-3), 5 star rating)

- Title and the beginning of the text about the video (written by the coach), i.e. about 30 words

- There are 2 sorts of videos.. (it's not necessary to explain why, it's just important that you implement two different versions of the video preview area (different only in terms of color!).. for example, some video preview areas could be edged in gold, others in silver.. or you could fill the whole video preview area with a color.. show me your taste... even though I prefer the more elegant way like gold and silver, you can probably surprise me with other color combinations..

- In order to simplify the process of comparing your designs, pls create 4 such preview video are areas..

6. Best voted video reviewer:

Users AND coaches will be able to write reviews about the videos. These reviews can be liked/voted. Therefore, we will know which user or coach writes the best reviews.

So we want you to implement also the charts of the 10 best voted video reviewers. Make sure there is a ranking list with the name of the user/coach and how many likes he got.
Here as well: add country flag, country and city (to see where they come from)..plus a little thumbnail of the profile picture.. Make sure the best 3 are being highlighted somehow..
Updates

Some designs were quite creative so far.
But unfortunately, less than half of the designers considered all requirements.
Therefore, be sure to implement all the requirements (for example, check new point nr. 6).
Without considering all the requirements, you don't have a chance to win this content.

Thank you.

Target Market(s)

male, 16-40 years old, worldwide audience

Industry/Entity Type

Dating

Requirements
Must have
• Not all submitted designs considered all requirements.

Therefore, please read the requirements carefully and consider all of them. If you want to add some new ideas or if you decide not to implement some requirements, I suggest to submit a second design.
Nice to have
• - if you have other ideas, feel free to add some of them to the front page, probably in form of a second design

- sometimes the same page will look totally different in other colors. Therefore, it would be great to add a 2nd version of your design, in terms of color

- the front page needs to be an eye-catcher

- different FLIRTNOVA font styles (come up with your own taste), a few different styles would be great!
Should not have
• - a search field like there is one in the first submitted design (the intelligent search is already being available with the filter system and the tags)

- female colors like pink/purple (it's a site only for men)

- a 08/15 look.. this will be the first website worldwide which contains videos from the best dating gurus on this planet in action.. they deserve a cool place to show their videos in order to gain new customers..

```html
<!DOCTYPE html>
<html lang="en">
<head>
<meta charset="utf-8">
<title>FLIRT NOVA – Infield Dating Videos</title>
<link href="https://fonts.googleapis.com/css2?family=Arimo:wght@400;700&family=Montserrat:wght@600;700&display=swap" rel="stylesheet">
<style>
:root{
  --page:#dbe5ee;
  --header-dark:#333;
  --header-mid:#4a4a4a;
  --gold:#f2c200;
  --gold-soft:#f7d84a;
  --silver:#bdbdbd;
  --blue:#2c4f8c;
  --blue-deep:#1f3b6e;
  --blue-accent:#3f6fb5;
  --panel:#f4f6f8;
  --panel-edge:#a9c4dc;
  --ink:#222;
  --muted:#888;
  --line:#d6dbe0;
  --white:#fff;
}
*{box-sizing:border-box;margin:0;padding:0}
html,body{width:720px;height:1200px;overflow:hidden;background:var(--page)}
body{font-family:"Arimo",Arial,sans-serif;color:var(--ink);position:relative}
.abs{position:absolute}

/* header */
.site-header{position:absolute;left:0;top:0;width:720px;height:199px;
  background:linear-gradient(180deg,var(--header-mid),var(--header-dark))}
.account{position:absolute;left:456px;top:10px;display:flex;gap:5px;align-items:center;font-size:8px;color:#bbb}
.account .field{width:60px;height:13px;background:#2a2a2a;border:1px solid #555;color:#999;font-size:7px;padding:2px 4px}
.account .go{width:16px;height:13px;background:#2a2a2a;border:1px solid #555;color:#ccc;font-size:6px;text-align:center;line-height:11px}
.account-rule{position:absolute;left:456px;top:32px;width:186px;height:1px;background:#555}
.brand{position:absolute;left:76px;top:90px;display:flex;align-items:center;gap:8px;
  font-family:"Montserrat",Arial,sans-serif;font-weight:700;font-size:17px;color:var(--gold);letter-spacing:.5px}
.brand .mark{width:12px;height:12px;background:var(--gold)}
.nav{position:absolute;right:77px;top:96px;display:flex;gap:21px;font-weight:700;font-size:10px;color:var(--gold)}
.claims{position:absolute;left:77px;top:128px;color:var(--white);font-weight:700;font-size:10px;line-height:28px}
.claims .hl{color:var(--gold)}
.counter{display:inline-flex;gap:2px;margin:0 4px;vertical-align:middle}
.counter span{width:12px;height:18px;background:var(--white);border:1px solid #999;color:#333;
  font-size:11px;text-align:center;line-height:16px;border-radius:2px}

/* search */
.search-tab{position:absolute;left:78px;top:223px;width:126px;height:40px;background:var(--panel);
  border-radius:4px 4px 0 0;font-weight:700;font-size:10px;padding:19px 0 0 42px}
.search-tab svg{position:absolute;left:18px;top:14px}
.search-panel{position:absolute;left:78px;top:262px;width:564px;height:166px;background:var(--panel);
  border-bottom:4px solid var(--panel-edge);border-radius:0 4px 4px 4px}
.label{position:absolute;font-weight:700;font-size:10px;color:var(--blue);line-height:12px}
.select{position:absolute;width:155px;height:22px;border-radius:2px;font-size:7px;font-weight:700;
  padding:7px 9px;color:var(--white)}
.select.active{background:linear-gradient(var(--blue-accent),var(--blue-deep))}
.select.idle{background:linear-gradient(#d0d0d0,#b5b5b5);color:#eee}
.select svg{position:absolute;right:7px;top:6px}
.tip{position:absolute;left:15px;top:134px;font-size:9px;font-family:Georgia,serif;display:flex;align-items:center;gap:8px}
.tip .i{width:18px;height:18px;border-radius:50%;background:#333;color:var(--white);font-weight:700;
  font-size:10px;text-align:center;line-height:18px;font-family:Georgia,serif}
.go-btn{position:absolute;left:530px;top:133px;width:24px;height:24px;background:var(--blue-deep);
  border-radius:3px;color:var(--gold);font-size:7px;font-weight:700;text-align:center;line-height:24px}

/* videos */
.videos{position:absolute;left:78px;top:446px;width:564px;height:382px;background:var(--panel);
  border-bottom:4px solid var(--panel-edge);border-radius:4px}
.row-rule{position:absolute;left:10px;top:168px;width:544px;border-top:1px dashed var(--line)}
.card{position:absolute;width:270px;height:156px}
.card .avatar{position:absolute;left:0;top:0;width:24px;height:24px;background:var(--white);border:1px solid #ccc}
.card .coach{position:absolute;left:32px;top:8px;font-size:7px;color:#333;letter-spacing:.5px}
.card .points{position:absolute;right:0;top:8px;font-size:7px;color:#333;letter-spacing:.5px}
.thumb{position:absolute;left:0;top:36px;width:112px;height:112px;border:4px solid var(--silver)}
.card.premium .thumb{border-color:var(--gold)}
.thumb .play{position:absolute;left:44px;top:42px}
.info{position:absolute;left:122px;top:34px;width:148px}
.info .title{font-size:7.5px;font-weight:700;color:var(--blue);text-decoration:underline;white-space:nowrap;letter-spacing:.3px}
.stats{display:grid;grid-template-columns:1fr 1fr;font-size:7px;color:var(--muted);line-height:8.5px;margin-top:3px}
.stars{display:flex;gap:2px;margin-top:4px}
.audio{font-size:7px;font-weight:700;margin-top:4px}
.audio b{color:var(--blue-accent)}
.excerpt{font-size:7.5px;line-height:9px;margin-top:6px}
.pager{position:absolute;left:0;top:346px;width:564px;height:32px;background:#eceef0;border-top:1px solid var(--line);
  font-size:8px;color:#999;font-weight:700}
.pager .prev{position:absolute;left:12px;top:12px}
.pager .next{position:absolute;right:12px;top:12px}
.pages{position:absolute;left:254px;top:8px;display:flex;gap:6px}
.pages span{width:14px;height:15px;border:1px solid #ccc;text-align:center;line-height:13px;font-weight:400;color:#777;background:var(--white)}
.pages .on{background:var(--gold);border-color:var(--gold);color:#333}

/* lower */
.col-title{position:absolute;top:848px;font-weight:700;font-size:9px}
.tags .letter{position:absolute;font-size:7px;font-weight:700;color:var(--blue-accent);line-height:7px;width:8px}
.tags .word{position:absolute;font-size:9px;line-height:11px}
.ranking{position:absolute;top:872px;width:160px}
.rank{height:25px;margin-bottom:3px;background:var(--white);position:relative;border:1px solid #e0e4e8}
.rank.first{background:var(--gold);border-color:var(--gold)}
.rank.podium{background:#c9c9c9;border-color:#c9c9c9}
.rank .pic{position:absolute;left:4px;top:3px;width:18px;height:18px;background:var(--white);border:1px solid #bbb}
.rank .name{position:absolute;left:28px;top:4px;font-size:7px;font-weight:700;letter-spacing:.3px}
.rank .loc{position:absolute;left:28px;top:14px;font-size:6px;color:#444;display:flex;gap:3px;align-items:center}
.rank .likes{position:absolute;right:5px;top:9px;font-size:6.5px;font-weight:700}
.footer-rule{position:absolute;left:78px;top:1166px;width:564px;height:1px;background:#b9c6d2}
.footer{position:absolute;left:0;top:1178px;width:720px;text-align:center;font-size:7px;color:#555}
</style>
</head>
<body>

<header class="site-header">
  <div class="account">Account <span class="field">login</span><span class="field">password</span><span class="go">GO</span></div>
  <div class="account-rule"></div>
  <div class="brand"><span class="mark"></span>FLIRT NOVA</div>
  <nav class="nav"><span>Contact</span><span>About</span><span>Sign In</span><span>Sign Up</span></nav>
  <div class="claims">
    <div>Because<span class="counter"><span>4</span><span>2</span><span>8</span></span>videos prove how to get <span class="hl">every woman</span> you want.</div>
    <div>Connect directly with<span class="counter"><span>3</span><span>6</span></span>dating-coaches from these videos!</div>
  </div>
</header>

<!-- search -->
<div class="search-tab">
  <svg width="14" height="16" viewBox="0 0 14 16"><path d="M2 1h10l-3 5 3 5H4v4H2z" fill="#7fb6e0"/></svg>
  Search Videos
</div>
<section class="search-panel">
  <div class="label" style="left:14px;top:10px">Language</div>
  <div class="select active" style="left:89px;top:6px">Polish, English, Spanish<svg width="6" height="10" viewBox="0 0 6 10"><path d="M0 4l3-4 3 4zM0 6l3 4 3-4z" fill="#fff"/></svg></div>
  <div class="label" style="left:14px;top:40px">Country</div>
  <div class="select active" style="left:89px;top:36px">USA, Poland<svg width="6" height="10" viewBox="0 0 6 10"><path d="M0 4l3-4 3 4zM0 6l3 4 3-4z" fill="#fff"/></svg></div>
  <div class="label" style="left:14px;top:70px">City</div>
  <div class="select idle" style="left:89px;top:66px">Undefined<svg width="6" height="10" viewBox="0 0 6 10"><path d="M0 4l3-4 3 4zM0 6l3 4 3-4z" fill="#fff"/></svg></div>
  <div class="label" style="left:14px;top:94px">Conversation<br>Starter</div>
  <div class="select idle" style="left:89px;top:96px">Undefined<svg width="6" height="10" viewBox="0 0 6 10"><path d="M0 4l3-4 3 4zM0 6l3 4 3-4z" fill="#fff"/></svg></div>

  <div class="label" style="left:287px;top:16px">Rating</div>
  <svg class="abs" style="left:384px;top:2px" width="160" height="30" viewBox="0 0 160 30">
    <g font-family="Arimo,Arial,sans-serif" font-size="7" fill="#2c4f8c" text-anchor="middle">
      <text x="7" y="8">1</text><text x="40" y="8">2</text><text x="72" y="8">3</text><text x="104" y="8">4</text><text x="137" y="8">5</text>
    </g>
    <line x1="7" y1="22" x2="137" y2="22" stroke="#b9c3cf" stroke-width="2"/>
    <line x1="40" y1="22" x2="137" y2="22" stroke="#2c4f8c" stroke-width="2"/>
    <circle cx="40" cy="22" r="5" fill="#fff" stroke="#2c4f8c" stroke-width="2"/>
    <circle cx="137" cy="22" r="5" fill="#fff" stroke="#2c4f8c" stroke-width="2"/>
  </svg>
  <div class="label" style="left:287px;top:46px">Level of Difficulty</div>
  <svg class="abs" style="left:378px;top:34px" width="170" height="30" viewBox="0 0 170 30">
    <g font-family="Arimo,Arial,sans-serif" font-size="6.5" fill="#2c4f8c" text-anchor="middle">
      <text x="16" y="8">Super easy</text><text x="86" y="8">Medium</text><text x="154" y="8">Expert</text>
    </g>
    <line x1="8" y1="22" x2="160" y2="22" stroke="#b9c3cf" stroke-width="2"/>
    <line x1="96" y1="22" x2="130" y2="22" stroke="#2c4f8c" stroke-width="2"/>
    <circle cx="96" cy="22" r="5" fill="#fff" stroke="#2c4f8c" stroke-width="2"/>
    <circle cx="130" cy="22" r="5" fill="#fff" stroke="#2c4f8c" stroke-width="2"/>
  </svg>
  <div class="label" style="left:287px;top:80px">Set-Size</div>
  <div class="select idle" style="left:384px;top:70px">Undefined<svg width="6" height="10" viewBox="0 0 6 10"><path d="M0 4l3-4 3 4zM0 6l3 4 3-4z" fill="#fff"/></svg></div>

  <div class="tip"><span class="i">i</span>Tip: You can select more positions holding CTRL.</div>
  <div class="go-btn">GO</div>
</section>

<!-- video previews -->
<section class="videos">
  <div class="row-rule"></div>

  <article class="card" style="left:12px;top:14px">
    <div class="avatar"></div><div class="coach">Marco Velante</div><div class="points">need 30 points</div>
    <div class="thumb" role="img" aria-label="Video thumbnail: city rooftops at dusk" style="background:linear-gradient(160deg,#2b3f66,#6a7ea0 55%,#c9a05a)"></div>
    <div class="info">
      <div class="title">Nam blandit, augue vel laoreet</div>
      <div class="stats"><span>62 221 views</span><span>Language: English</span><span>Difficulty: Medium</span><span>USA ▪</span><span>3:21</span><span>New York</span></div>
      <svg class="stars" width="60" height="10" viewBox="0 0 60 10"><g fill="#f2c200"><path id="s" d="M5 0l1.5 3.3 3.5.4-2.6 2.3.8 3.5L5 7.7 1.8 9.5l.8-3.5L0 3.7l3.5-.4z"/><use href="#s" x="12"/><use href="#s" x="24"/></g><g fill="#ccc"><use href="#s" x="36"/><use href="#s" x="48"/></g></svg>
      <div class="audio">Audio comment: <b>No</b></div>
      <div class="excerpt">Elementum ligula, quis congue nunc nisl eu urna. Nam euismod velit aliquam massa.</div>
    </div>
  </article>

  <article class="card premium" style="left:280px;top:14px">
    <div class="avatar"></div><div class="coach">Tomas Reyes</div><div class="points">need 20 points</div>
    <div class="thumb" role="img" aria-label="Video thumbnail: harbour bridge under a blue evening sky" style="background:linear-gradient(170deg,#1e4f9c,#4f86c8 55%,#b79a62)"></div>
    <div class="info">
      <div class="title">In ac dui sapien, donec</div>
      <div class="stats"><span>520 186 views</span><span>Language: English</span><span>Difficulty: easy</span><span>USA ▪</span><span>5:13</span><span>New York</span></div>
      <svg class="stars" width="60" height="10" viewBox="0 0 60 10"><g fill="#f2c200"><use href="#s"/><use href="#s" x="12"/><use href="#s" x="24"/><use href="#s" x="36"/></g><use href="#s" x="48" fill="#ccc"/></svg>
      <div class="audio">Audio comment: <b>Yes</b></div>
      <div class="excerpt">In at dui sapien. Donec sed aliquam elit. Quisque vitae lacinia erat. Mauris venenatis nisi quis massa porta iaculis. Nulla odio ipsum, accumsan…</div>
    </div>
  </article>

  <article class="card" style="left:12px;top:178px">
    <div class="avatar"></div><div class="coach">Ivan Brec</div><div class="points">need 10 points</div>
    <div class="thumb" role="img" aria-label="Video thumbnail: seafront lights at blue hour" style="background:linear-gradient(180deg,#2a5fb0,#3c78c6 60%,#d0a24a)">
      <svg class="play" width="14" height="16" viewBox="0 0 14 16"><path d="M0 0l14 8-14 8z" fill="#1a2a44"/></svg></div>
    <div class="info">
      <div class="title">Nulla auctor mollis</div>
      <div class="stats"><span>620 862 views</span><span>Language: English</span><span>Difficulty: easy</span><span>USA ▪</span><span>0:45</span><span>New York</span></div>
      <svg class="stars" width="60" height="10" viewBox="0 0 60 10"><use href="#s" fill="#f2c200"/><g fill="#ccc"><use href="#s" x="12"/><use href="#s" x="24"/><use href="#s" x="36"/><use href="#s" x="48"/></g></svg>
      <div class="audio">Audio comment: <b>No</b></div>
      <div class="excerpt">Vivamus tempus, nulla ut cursus vulputate, nibh ipsum vehicula diam, in facilisis enim lorem vitae eros. Maecenas laoreet nulla in ante.</div>
    </div>
  </article>

  <article class="card premium" style="left:280px;top:178px">
    <div class="avatar"></div><div class="coach">Luca Ferro</div><div class="points">need 30 points</div>
    <div class="thumb" role="img" aria-label="Video thumbnail: old town street at night" style="background:linear-gradient(160deg,#3a3540,#8a6a3e 55%,#e0a640)">
      <svg class="play" width="14" height="16" viewBox="0 0 14 16"><path d="M0 0l14 8-14 8z" fill="#1a1a1a"/></svg></div>
    <div class="info">
      <div class="title">Aliquam vitae lectus sed</div>
      <div class="stats"><span>1 800 views</span><span>Language: English</span><span>Difficulty: Expert</span><span>USA ▪</span><span>1:23</span><span>New York</span></div>
      <svg class="stars" width="60" height="10" viewBox="0 0 60 10"><g fill="#f2c200"><use href="#s"/><use href="#s" x="12"/><use href="#s" x="24"/><use href="#s" x="36"/></g><use href="#s" x="48" fill="#ccc"/></svg>
      <div class="audio">Audio comment: <b>No</b></div>
      <div class="excerpt">Aliquam erat justo, vulputate vel pharetra tempus, imperdiet a nulla.</div>
    </div>
  </article>

  <nav class="pager">
    <span class="prev">◂ Previous</span>
    <div class="pages"><span>1</span><span class="on">2</span><span>3</span></div>
    <span class="next">Next ▸</span>
  </nav>
</section>

<!-- tags -->
<section class="tags">
  <div class="col-title" style="left:144px">Tags</div>
  <div class="letter" style="left:79px;top:868px">A</div><div class="word" style="left:87px;top:874px">amet</div>
  <div class="letter" style="left:79px;top:892px">B</div><div class="word" style="left:87px;top:899px">bitch shield, bounce,<br>blow out opener</div>
  <div class="letter" style="left:79px;top:930px">C</div><div class="word" style="left:87px;top:937px">calibration,<br>canned rouine</div>
  <div class="letter" style="left:79px;top:964px">D</div><div class="word" style="left:87px;top:971px">dolor</div>
  <div class="letter" style="left:79px;top:990px">E<br>F</div><div class="word" style="left:87px;top:1005px">feugiat</div>
  <div class="letter" style="left:79px;top:1024px">G<br>H<br>I</div><div class="word" style="left:87px;top:1046px">integer</div>
  <div class="letter" style="left:190px;top:874px">J<br>K<br>L<br>M</div><div class="word" style="left:196px;top:902px">mollis</div>
  <div class="letter" style="left:190px;top:922px">N<br>O<br>P<br>Q<br>R<br>S</div><div class="word" style="left:196px;top:970px">semper</div>
  <div class="letter" style="left:190px;top:990px">T<br>U<br>V</div><div class="word" style="left:196px;top:1012px">vestibulum</div>
  <div class="letter" style="left:190px;top:1032px">W</div>
</section>

<!-- rankings -->
<div class="col-title" style="left:311px">Best rated reviewers</div>
<ol class="ranking" style="left:282px;list-style:none">
  <li class="rank first"><span class="pic"></span><span class="name">Commodo egestas</span><span class="loc">New York in USA ▪</span><span class="likes">1345 likes</span></li>
  <li class="rank podium"><span class="pic"></span><span class="name">Commodo egestas</span><span class="loc">New York in USA ▪</span><span class="likes">794 likes</span></li>
  <li class="rank podium"><span class="pic"></span><span class="name">Commodo egestas</span><span class="loc">New York in USA ▪</span><span class="likes">769 likes</span></li>
  <li class="rank"><span class="pic"></span><span class="name">Commodo egestas</span><span class="loc">New York in USA ▪</span><span class="likes">511 likes</span></li>
  <li class="rank"><span class="pic"></span><span class="name">Commodo egestas</span><span class="loc">New York in USA ▪</span><span class="likes">455 likes</span></li>
  <li class="rank"><span class="pic"></span><span class="name">Commodo egestas</span><span class="loc">New York in USA ▪</span><span class="likes">403 likes</span></li>
  <li class="rank"><span class="pic"></span><span class="name">Commodo egestas</span><span class="loc">New York in USA ▪</span><span class="likes">399 likes</span></li>
  <li class="rank"><span class="pic"></span><span class="name">Commodo egestas</span><span class="loc">New York in USA ▪</span><span class="likes">362 likes</span></li>
  <li class="rank"><span class="pic"></span><span class="name">Commodo egestas</span><span class="loc">New York in USA ▪</span><span class="likes">355 likes</span></li>
  <li class="rank"><span class="pic"></span><span class="name">Commodo egestas</span><span class="loc">New York in USA ▪</span><span class="likes">329 likes</span></li>
</ol>

<div class="col-title" style="left:510px">Best rated coaches</div>
<ol class="ranking" style="left:472px;list-style:none">
  <li class="rank first"><span class="pic"></span><span class="name">Commodo egestas</span><span class="loc">New York in USA ▪</span><span class="likes">1345 likes</span></li>
  <li class="rank podium"><span class="pic"></span><span class="name">Commodo egestas</span><span class="loc">New York in USA ▪</span><span class="likes">794 likes</span></li>
  <li class="rank podium"><span class="pic"></span><span class="name">Commodo egestas</span><span class="loc">New York in USA ▪</span><span class="likes">769 likes</span></li>
  <li class="rank"><span class="pic"></span><span class="name">Commodo egestas</span><span class="loc">New York in USA ▪</span><span class="likes">511 likes</span></li>
  <li class="rank"><span class="pic"></span><span class="name">Commodo egestas</span><span class="loc">New York in USA ▪</span><span class="likes">455 likes</span></li>
  <li class="rank"><span class="pic"></span><span class="name">Commodo egestas</span><span class="loc">New York in USA ▪</span><span class="likes">403 likes</span></li>
  <li class="rank"><span class="pic"></span><span class="name">Commodo egestas</span><span class="loc">New York in USA ▪</span><span class="likes">399 likes</span></li>
  <li class="rank"><span class="pic"></span><span class="name">Commodo egestas</span><span class="loc">New York in USA ▪</span><span class="likes">362 likes</span></li>
  <li class="rank"><span class="pic"></span><span class="name">Commodo egestas</span><span class="loc">New York in USA ▪</span><span class="likes">355 likes</span></li>
  <li class="rank"><span class="pic"></span><span class="name">Commodo egestas</span><span class="loc">New York in USA ▪</span><span class="likes">329 likes</span></li>
</ol>

<div class="footer-rule"></div>
<footer class="footer">Copyright © 2012 All rights reserved.</footer>

</body>
</html>
```